Graphics for website image slider

We need 4 banners for website:

We provide software development services to very small to large Businesses. The focus of these 4 banners is to portray the four steps approach to our consulting process: Assess, Analyse, Plan and Deploy

Currently we have the following on our website:
http://www.lumertix.com

We are redesigning the website and want to use 4 sliding graphics to portray the same thing, and the new site is being designed here:
http://www.lumertixonline.com/lumertix

You can use stock photos for each banner or your own creativity.

The images should be 1140px wide and about 420px High.

You can use any modern font such as google font. Not just curly fonts!

Reason: Not yet able to select the final design.

I have updated the colors and how they are supposed to flow because I noticed that some designs did not follow that (We are consultants and really want to understand our process in a powerful way):

ASSESS: Orange color (1st or 5th color above)

ANALYSE: Yellow (2nd or 6th color above)

PLAN: Green (3rd or 7th color above)

DEPLOY: Blue (4th or 8th color above)

=================================================

Some designers also made mistakes in typing the text (Please copy and paste from below):

ASSESS

We gather information and data

to identify and delineate

your central and most pressing business and IT issues.

ANALYSE

We show you exactly where you are in terms of IT maturity

using our optimization tools.

We then build an IT roadmap to help you get to the next level.

PLAN:

We identify the IT products and processes necessary to implement the solution.

We then create a detailed plan of action and technical specifications.

DEPLOY

Finally, we utilize industry best practices and repeatable development and

deployment methods to ensure efficiency and high quality results

that satisfy and bring improvement within budget and timeline.

                                   

Target Market(s)

http://www.lumertix.com

Industry/Entity Type

Software

Font styles to use
Sans Serif
Other font styles liked:
• Any other modern font (No curly fonts)

Colors
fee18a
fbf289
cadf82
86cae6
f78f20
ffc214
9aca3c
0692cd

Requirements
Must have
• Graphic should convey the message for each process

```html
<!DOCTYPE html>
<html lang="en">
<head>
<meta charset="utf-8">
<title>Lumertix Consulting Process Banners</title>
<link rel="stylesheet" href="https://fonts.googleapis.com/css2?family=Open+Sans:wght@700;800&family=PT+Sans:wght@400&display=swap">
<style>
  :root {
    --orange: #f78f20;
    --orange-deep: #f26a1b;
    --orange-light: #fdb862;
    --yellow: #ffc214;
    --yellow-light: #fbf289;
    --yellow-pale: #fee18a;
    --green: #9aca3c;
    --green-deep: #6fa521;
    --green-light: #cadf82;
    --blue: #0692cd;
    --blue-light: #86cae6;
    --blue-pale: #cfe9f5;
    --ink: #1f1f1f;
    --suit: #2a2d38;
  }
  * { margin: 0; padding: 0; box-sizing: border-box; }
  html, body { width: 796px; height: 1200px; overflow: hidden; background: #ffffff; }
  .canvas { position: relative; width: 796px; height: 1200px; overflow: hidden; }

  .banner { position: absolute; left: 0; width: 796px; overflow: hidden; }
  .banner-assess  { top: 0;     height: 296px; background: linear-gradient(180deg, var(--yellow) 0%, var(--orange-light) 45%, var(--orange) 100%); }
  .banner-analyse { top: 296px; height: 300px; background: linear-gradient(90deg, var(--orange-light) 0%, var(--yellow) 40%, var(--yellow-light) 100%); }
  .banner-plan    { top: 596px; height: 303px; background: linear-gradient(180deg, var(--green-light) 0%, #dcec9c 50%, var(--green-light) 100%); }
  .banner-deploy  { top: 899px; height: 301px; background: linear-gradient(180deg, var(--blue-light) 0%, var(--blue-pale) 60%, var(--blue-light) 100%); }

  .stripe { position: absolute; left: 0; top: 0; width: 796px; height: 9px; }
  .banner-assess .stripe  { background: var(--orange); }
  .banner-analyse .stripe { background: var(--yellow); height: 11px; }
  .banner-plan .stripe    { background: var(--green); }
  .banner-deploy .stripe  { background: var(--blue); }

  .text-panel { position: absolute; left: 0; width: 796px; background: rgba(255,255,255,0.16); }
  .banner-assess .text-panel  { top: 88px; height: 194px; }
  .banner-analyse .text-panel { top: 62px; height: 224px; }
  .banner-plan .text-panel    { top: 62px; height: 222px; }
  .banner-deploy .text-panel  { top: 30px; height: 250px; }

  .step-title {
    position: absolute;
    font-family: "Open Sans", Arial, sans-serif;
    font-weight: 800;
    font-size: 46px;
    line-height: 1;
    letter-spacing: 0.5px;
  }
  .banner-assess .step-title  { left: 32px;  top: 116px; color: var(--orange-deep); }
  .banner-analyse .step-title { left: 346px; top: 92px;  color: var(--orange); }
  .banner-plan .step-title    { left: 32px;  top: 90px;  color: var(--green-deep); }
  .banner-deploy .step-title  { left: 354px; top: 63px;  color: var(--blue); }

  .step-copy {
    position: absolute;
    font-family: "PT Sans", Arial, sans-serif;
    font-size: 19px;
    line-height: 25.5px;
    color: var(--ink);
    white-space: nowrap;
  }
  .banner-assess .step-copy  { left: 29px;  top: 172px; }
  .banner-analyse .step-copy { left: 343px; top: 148px; }
  .banner-plan .step-copy    { left: 29px;  top: 148px; }
  .banner-deploy .step-copy  { left: 352px; top: 122px; }

  .photo { position: absolute; }
  .banner-assess .photo  { left: 399px; top: 17px; width: 381px; height: 273px; background: linear-gradient(90deg, rgba(42,45,56,0) 0%, rgba(42,45,56,0.55) 35%, var(--suit) 70%, rgba(42,45,56,0.8) 100%); }
  .banner-analyse .photo { left: 0;     top: 11px; width: 193px; height: 280px; background: linear-gradient(135deg, var(--suit) 0%, #4a4f5e 55%, #e9e9e9 100%); }
  .banner-plan .photo    { left: 443px; top: 28px; width: 353px; height: 263px; background: linear-gradient(180deg, rgba(42,45,56,0.35) 0%, var(--suit) 55%, #5b5f6a 100%); }
  .banner-deploy .photo  { left: 13px;  top: 13px; width: 316px; height: 272px; background: linear-gradient(180deg, rgba(42,45,56,0.4) 0%, var(--suit) 40%, #3a3d48 100%); }
</style>
</head>
<body>
<main class="canvas">

  <section class="banner banner-assess">
    <div class="stripe"></div>
    <div class="text-panel"></div>
    <div class="photo" role="img" aria-label="Stock photo of a smiling businessman and businesswoman in dark suits, the man gesturing toward the text"></div>
    <h2 class="step-title">ASSESS</h2>
    <div class="step-copy">
      &nbsp;&nbsp;&nbsp;&nbsp;We gather information and data to<br>
      identify and delineate your central and<br>
      most pressing business and IT issues.
    </div>
  </section>

  <section class="banner banner-analyse">
    <div class="stripe"></div>
    <div class="text-panel"></div>
    <div class="photo" role="img" aria-label="Stock photo of two business colleagues reviewing documents together at a desk"></div>
    <h2 class="step-title">ANALYSE</h2>
    <div class="step-copy">
      &nbsp;&nbsp;&nbsp;&nbsp;We show you exactly where you are in terms<br>
      of IT maturity using our optimization tools.<br>
      &nbsp;&nbsp;&nbsp;&nbsp;We then build an IT roadmap to help you get<br>
      to the next level.
    </div>
  </section>

  <section class="banner banner-plan">
    <div class="stripe"></div>
    <div class="text-panel"></div>
    <div class="photo" role="img" aria-label="Stock photo of a businessman and businesswoman smiling at a desk with a laptop and papers"></div>
    <h2 class="step-title">PLAN</h2>
    <div class="step-copy">
      &nbsp;&nbsp;&nbsp;&nbsp;We identify the IT products and processes<br>
      necessary to implement the solution.<br>
      &nbsp;&nbsp;&nbsp;&nbsp;We then create a detailed plan of action<br>
      and technical specifications.
    </div>
  </section>

  <section class="banner banner-deploy">
    <div class="stripe"></div>
    <div class="text-panel"></div>
    <div class="photo" role="img" aria-label="Stock photo of a team of five business people in suits standing together"></div>
    <h2 class="step-title">DEPLOY</h2>
    <div class="step-copy">
      &nbsp;&nbsp;&nbsp;&nbsp;Finally, we utilize industry best practices<br>
      and repeatable development and deployment<br>
      methods to ensure efficiency and high quality<br>
      results that satisfy and bring improvement<br>
      within budget and timeline.
    </div>
  </section>

</main>
</body>
</html>
```